Apartment Investor Business Card Design

Need a new business card designed for my multifamily investment company

Industry/Entity Type

Real Estate

Contact Information for Business Card

Garrick Pelham - President & CEO
Brightwold Holdings, LLC
4838 North 92nd Avenue, Ste 500
Omaha, NE 68999
(402) 555-0147
Garrick@brightwoldholdings.example
Www.BrightwoldHoldings.example

Colors
3176b5

```html
<!DOCTYPE html>
<html lang="en">
<head>
<meta charset="utf-8">
<title>Brightwold Holdings – Business Card</title>
<link href="https://fonts.googleapis.com/css2?family=Cinzel:wght@400;700&family=Questrial&display=swap" rel="stylesheet">
<style>
  :root {
    --page-bg: #d8d8d8;
    --card-dark: #2a2b2d;
    --card-mid: #3b3c3f;
    --blue-deep: #3176b5;
    --blue-light: #3d8fcf;
    --blue-accent: #3a87cc;
    --text-light: #ffffff;
  }
  * { box-sizing: border-box; margin: 0; padding: 0; }
  html, body {
    width: 960px;
    height: 1200px;
    overflow: hidden;
    background: var(--page-bg);
  }
  .card {
    position: absolute;
    left: 112px;
    width: 736px;
    height: 442px;
    overflow: hidden;
    background: radial-gradient(ellipse at 60% 45%, var(--card-mid) 0%, var(--card-dark) 75%);
  }
  .card--front { top: 84px; }
  .card--back { top: 672px; }
  .card__backdrop {
    position: absolute;
    inset: 0;
    background: linear-gradient(180deg, rgba(255,255,255,0.03) 0%, rgba(255,255,255,0) 60%);
  }
  .card__shapes {
    position: absolute;
    inset: 0;
    width: 100%;
    height: 100%;
  }
  .brand-name {
    position: absolute;
    font-family: "Cinzel", serif;
    font-weight: 400;
    color: var(--text-light);
    white-space: nowrap;
    transform: translateX(-50%);
  }
  .brand-name--front {
    left: 531px;
    top: 250px;
    font-size: 28px;
    letter-spacing: 1px;
  }
  .brand-name--back {
    left: 632px;
    top: 388px;
    font-size: 12px;
  }
  .holder {
    position: absolute;
    left: 41px;
    top: 24px;
  }
  .holder__name {
    font-family: "Cinzel", serif;
    font-weight: 700;
    font-size: 27px;
    letter-spacing: 2px;
    color: var(--text-light);
    line-height: 1;
  }
  .holder__title {
    font-family: "Questrial", sans-serif;
    font-size: 14px;
    letter-spacing: 3px;
    color: var(--blue-accent);
    margin-top: 5px;
  }
  .contact-list {
    position: absolute;
    left: 40px;
    top: 0;
    list-style: none;
  }
  .contact-item {
    position: absolute;
    left: 0;
    display: flex;
    align-items: center;
    white-space: nowrap;
  }
  .contact-item__icon {
    width: 34px;
    height: 34px;
    border-radius: 50%;
    background: var(--blue-deep);
    display: flex;
    align-items: center;
    justify-content: center;
    flex-shrink: 0;
  }
  .contact-item__icon svg { width: 19px; height: 19px; }
  .contact-item__text {
    margin-left: 24px;
    font-family: "Questrial", sans-serif;
    font-size: 17px;
    line-height: 17px;
    color: var(--text-light);
  }
  .contact-item--address { top: 157px; }
  .contact-item--phone { top: 210px; }
  .contact-item--email { top: 262px; }
  .contact-item--web { top: 315px; }
</style>
</head>
<body>

<section class="card card--front">
  <div class="card__backdrop" role="img" aria-label="Faint stock market candlestick chart in the dark background"></div>
  <svg class="card__shapes" viewBox="0 0 920 552" preserveAspectRatio="none" aria-hidden="true">
    <defs>
      <filter id="band-shadow" x="-20%" y="-20%" width="140%" height="140%">
        <feDropShadow dx="4" dy="4" stdDeviation="6" flood-color="#000" flood-opacity="0.45"/>
      </filter>
    </defs>
    <polygon points="275,0 457,0 367,160" fill="var(--blue-deep)" filter="url(#band-shadow)"/>
    <polygon points="465,85 487,130 367,335 489,552 192,552" fill="var(--blue-deep)" filter="url(#band-shadow)"/>
    <polygon points="457,0 487,38 192,552 142,552" fill="var(--blue-light)" filter="url(#band-shadow)"/>
  </svg>
  <div class="brand-name brand-name--front">BRIGHTWOLD HOLDINGS</div>
</section>

<section class="card card--back">
  <div class="card__backdrop" role="img" aria-label="Faint stock market candlestick chart in the dark background"></div>
  <svg class="card__shapes" viewBox="0 0 920 552" preserveAspectRatio="none" aria-hidden="true">
    <defs>
      <filter id="band-shadow-back" x="-20%" y="-20%" width="140%" height="140%">
        <feDropShadow dx="-4" dy="4" stdDeviation="6" flood-color="#000" flood-opacity="0.45"/>
      </filter>
    </defs>
    <polygon points="554,0 694,0 586,190 519,70" fill="var(--blue-deep)" filter="url(#band-shadow-back)"/>
    <polygon points="674,340 719,410 649,552 549,552" fill="var(--blue-deep)" filter="url(#band-shadow-back)"/>
    <polygon points="519,70 472,152 579,330 454,552 549,552 674,340" fill="var(--blue-light)" filter="url(#band-shadow-back)"/>
  </svg>

  <header class="holder">
    <h1 class="holder__name">GARRICK PELHAM</h1>
    <p class="holder__title">PRESIDENT &amp; CEO</p>
  </header>

  <ul class="contact-list">
    <li class="contact-item contact-item--address">
      <span class="contact-item__icon">
        <svg viewBox="0 0 24 24" fill="none" stroke="#fff" stroke-width="1.8" stroke-linejoin="round"><path d="M3 11 12 3l9 8v10h-6v-6H9v6H3z"/></svg>
      </span>
      <span class="contact-item__text">Brightwold Holdings, LLC<br>4838 North 92nd Ave., Ste 500<br>Omaha, NE 68999</span>
    </li>
    <li class="contact-item contact-item--phone">
      <span class="contact-item__icon">
        <svg viewBox="0 0 24 24" fill="none" stroke="#fff" stroke-width="1.8" stroke-linejoin="round"><path d="M5 3h4l2 5-2.5 1.5a11 11 0 0 0 6 6L16 13l5 2v4a2 2 0 0 1-2 2A16 16 0 0 1 3 5a2 2 0 0 1 2-2z"/></svg>
      </span>
      <span class="contact-item__text">(402) 555 - 0147</span>
    </li>
    <li class="contact-item contact-item--email">
      <span class="contact-item__icon">
        <svg viewBox="0 0 24 24" fill="none" stroke="#fff" stroke-width="1.8" stroke-linejoin="round"><rect x="3" y="5" width="18" height="14"/><path d="m3 5 9 8 9-8"/></svg>
      </span>
      <span class="contact-item__text">Garrick@brightwoldholdings.example</span>
    </li>
    <li class="contact-item contact-item--web">
      <span class="contact-item__icon">
        <svg viewBox="0 0 24 24" fill="none" stroke="#fff" stroke-width="1.6"><circle cx="12" cy="12" r="9"/><ellipse cx="12" cy="12" rx="4" ry="9"/><path d="M3 12h18M5 7h14M5 17h14"/></svg>
      </span>
      <span class="contact-item__text">www.BrightwoldHoldings.example</span>
    </li>
  </ul>

  <div class="brand-name brand-name--back">BRIGHTWOLD HOLDINGS</div>
</section>

</body>
</html>
```